Verdant Tide Collective needs packaging design for 500g Hemp Seed Pouch

We need a packaging design for the release of our Australian sourced Super Healthy, Nutritious super food HEMP SEED.

The verdant Tide collective - food, fibre, fuel, building, medicine
We are a start up company who is very Passionate about Hemp, rebuilding the hemp industry through inspiration, education and distribution of all things hemp.

This Hemp Seed packaging will be our first product launch

Kernel of NUVA GRAINS 500gram

needs to communicate 3 things, that Hemp seeds:
1. TASTE GREAT
2. EASY TO USE
3. GOOD FOR YOU

other Features of hemp seeds is that they are :
Vegan
Paleo
Raw
Sustainable
High in protein
High in Omega 3 + 6 EFA
Anti allergenic

we would like to see designs that work with our current logo and colouring of orange and black. premium and stylish that says healthy

the pouches will be '500g' meaning they will hold 500grams of hulled hemp seeds.

with dimensions of
170mm x 250mm
see attached photo of competitors hemp protein pouch as example of pouch design

see attached for current logo designs and colouring
also see attached concept sketch we are not married to this sketch it is just as a guideline for elements that should be included.

final design should feel healthy clean and safe for consumption:)
with an emphasis on being PremiumAustralian seed soured from from pristine Tasmania

Health conscious

• map of Australia or show that it is Australian in some way
• Spoon of hemp seeds or picture of Nuva Kernels

```html
<!DOCTYPE html>
<html lang="en">
<head>
<meta charset="utf-8">
<title>Kernel of Nuva Grains – 500g Pouch</title>
<link href="https://fonts.googleapis.com/css2?family=Titan+One&family=Russo+One&family=Teko:wght@500;600&family=Saira+Condensed:wght@700;800&family=Playfair+Display:ital,wght@1,700&display=swap" rel="stylesheet">
<style>
  :root {
    --stage: #8f8f8f;
    --orange: #f7931e;
    --orange-deep: #e07c12;
    --black: #111111;
    --brown-dark: #2a2420;
    --green: #5aa845;
    --green-badge: #4f9a48;
    --cream: #fbe9cf;
    --white: #ffffff;
  }
  * { box-sizing: border-box; margin: 0; padding: 0; }
  html, body { width: 1200px; height: 1200px; overflow: hidden; }
  body {
    background: linear-gradient(180deg, #3c3c3c 0%, var(--stage) 55%, #a8a8a8 100%);
    position: relative;
  }
  .pouch {
    position: absolute; left: 200px; top: 45px;
    width: 800px; height: 1110px;
    border-radius: 70px 70px 24px 24px;
    overflow: hidden;
    background: linear-gradient(180deg, var(--orange) 0%, var(--orange) 52%, #b8650f 66%, #4a3322 84%, var(--brown-dark) 100%);
  }
  .pouch__art { position: absolute; inset: 0; }
  .leaf-art { position: absolute; }
  .banner {
    position: absolute; left: 56px; top: 100px; width: 688px; height: 72px;
    display: flex; align-items: center; justify-content: center;
  }
  .banner svg { position: absolute; inset: 0; }
  .banner__text {
    position: relative;
    font-family: "Playfair Display", serif; font-style: italic; font-weight: 700;
    font-size: 30px; color: var(--black);
  }
  .brand {
    position: absolute; left: 312px; top: 156px; width: 184px; height: 184px;
    border-radius: 50%; background: radial-gradient(circle, #fff8ee 0%, #ffd9a8 60%, var(--orange) 100%);
    display: flex; align-items: center; justify-content: center; text-align: center;
  }
  .brand__name {
    font-family: "Russo One", sans-serif; font-size: 22px; line-height: 1.1;
    color: var(--black); width: 130px;
  }
  .title { position: absolute; left: 0; width: 800px; text-align: center; }
  .title__lead {
    top: 360px; font-family: "Russo One", sans-serif; font-size: 54px;
    letter-spacing: 6px; color: var(--white);
  }
  .title__main {
    top: 420px; font-family: "Titan One", sans-serif; font-size: 96px;
    line-height: 1; color: var(--orange);
  }
  .tagline {
    position: absolute; top: 514px; left: 0; width: 800px;
    display: flex; justify-content: center; align-items: center; gap: 12px;
    font-family: "Teko", sans-serif; font-weight: 600; font-size: 36px;
    color: var(--white); letter-spacing: 1px;
  }
  .tagline__dot { width: 20px; height: 20px; border-radius: 50%; background: var(--orange); }
  .features { position: absolute; left: 64px; top: 704px; list-style: none; }
  .features__item {
    font-family: "Saira Condensed", sans-serif; font-weight: 800; font-size: 36px;
    line-height: 44px; color: var(--orange); text-transform: uppercase;
    border-bottom: 2px solid var(--orange); padding-right: 40px; margin-bottom: 2px;
    width: max-content;
  }
  .product-shot { position: absolute; left: 272px; top: 560px; width: 500px; height: 430px; }
  .badge { position: absolute; left: 572px; top: 830px; width: 150px; height: 130px; }
  .badge__text {
    position: absolute; inset: 30px 0 0 0; text-align: center;
    font-family: "Teko", sans-serif; font-weight: 500; font-size: 22px; line-height: 22px;
    color: var(--white); transform: rotate(-12deg);
  }
  .weight {
    position: absolute; left: 640px; top: 1010px;
    font-family: "Teko", sans-serif; font-weight: 500; font-size: 36px; color: var(--orange);
  }
</style>
</head>
<body>
<main class="pouch">
  <svg class="pouch__art" width="800" height="1110" viewBox="0 0 800 1110">
    <polygon points="396,22 110,330 690,260" fill="var(--green)"/>
    <polygon points="396,40 130,330 670,270" fill="var(--black)"/>
    <rect x="0" y="330" width="800" height="232" fill="var(--black)"/>
    <polygon points="130,330 670,270 800,270 800,330" fill="var(--black)"/>
    <rect x="0" y="562" width="800" height="8" fill="var(--green)"/>
  </svg>

  <div class="leaf-art" role="img" aria-label="Green hemp leaf illustration on the left side"
       style="left:0;top:140px;width:260px;height:480px;background:radial-gradient(ellipse at 40% 50%, rgba(70,140,60,.85), rgba(70,140,60,0) 70%);"></div>
  <div class="leaf-art" role="img" aria-label="Green hemp leaf illustration on the right side"
       style="left:580px;top:220px;width:220px;height:300px;background:radial-gradient(ellipse at 60% 50%, rgba(70,140,60,.8), rgba(70,140,60,0) 70%);"></div>

  <div class="banner">
    <svg viewBox="0 0 688 72" preserveAspectRatio="none">
      <polygon points="0,20 90,20 90,60 0,60 30,40" fill="var(--black)"/>
      <polygon points="688,20 598,20 598,60 688,60 658,40" fill="var(--black)"/>
      <rect x="80" y="6" width="528" height="58" rx="8" fill="var(--cream)" stroke="var(--black)" stroke-width="4"/>
    </svg>
    <span class="banner__text">Nature’s Perfect Super Food</span>
  </div>

  <div class="brand"><span class="brand__name">Verdant Tide Collective</span></div>

  <h1>
    <span class="title title__lead">KERNEL OF</span>
    <span class="title title__main">Nuva Grains</span>
  </h1>

  <p class="tagline">
    <span>TASTE GREAT</span><span class="tagline__dot"></span>
    <span>EASY TO USE</span><span class="tagline__dot"></span>
    <span>GOOD FOR YOU</span>
  </p>

  <ul class="features">
    <li class="features__item">Vegan</li>
    <li class="features__item">Paleo</li>
    <li class="features__item">Raw</li>
    <li class="features__item">Sustainable</li>
    <li class="features__item">High in protein</li>
    <li class="features__item">High in Omega 3 + 6 EFA</li>
    <li class="features__item">Anti allergenic</li>
  </ul>

  <svg class="product-shot" viewBox="0 0 500 430" role="img"
       aria-label="Orange map of Australia behind a heart-shaped photo of hulled seeds with a spoonful of seeds">
    <defs>
      <linearGradient id="mapTone" x1="0" y1="0" x2="0" y2="1">
        <stop offset="0" stop-color="var(--orange)"/>
        <stop offset="1" stop-color="var(--orange-deep)"/>
      </linearGradient>
      <radialGradient id="seedTone" cx="0.5" cy="0.45" r="0.6">
        <stop offset="0" stop-color="#efe6cf"/>
        <stop offset="1" stop-color="#b9ad88"/>
      </radialGradient>
    </defs>
    <rect x="120" y="20" width="360" height="300" rx="60" fill="url(#mapTone)"/>
    <path d="M180,420 C60,330 0,260 0,180 C0,120 50,90 95,90 C140,90 170,120 180,150 C190,120 220,90 265,90 C310,90 360,120 360,180 C360,260 300,330 180,420 Z"
          fill="url(#seedTone)" stroke="var(--orange)" stroke-width="8"/>
    <ellipse cx="300" cy="170" rx="140" ry="70" fill="#ddd3b8"/>
  </svg>

  <div class="badge">
    <svg width="150" height="130" viewBox="0 0 150 130">
      <path d="M75,128 C25,95 0,70 0,40 C0,15 20,0 42,0 C58,0 70,10 75,22 C80,10 92,0 108,0 C130,0 150,15 150,40 C150,70 125,95 75,128 Z" fill="var(--green-badge)"/>
    </svg>
    <p class="badge__text">PRRMIUM<br>TASMANIAN SEED</p>
  </div>

  <p class="weight">500g</p>
</main>
</body>
</html>
```